Flyer for annual KESTREL SUMMIT 2020

I would like a church event flyer designed. The event is called "KESTREL SUMMIT 2020". I am looking for a professional, yet catchy design that uses our brand colors and logo creatively while communicating key information of the event effectively.

1. The logo is attached in two color formats. The designer has the choice to use them as he/she want.

2. The location of the event is: Harlow Community Center, 239 Fennimore Street, Portland, ME 04117

3. Time and date of event. The designer can organize and format the date and time as he/she pleases.
Thursday December 31st @ 6:30PM
Friday January 1st @ 6:30PM
Saturday 2nd @ 6:30PM
Sunday 3rd @ 4:30PM

4. The topic of the event is "In Fire and On Fire". The designer is free to use this phrase as he/she pleases to create a good composition.

5. Speaker: Prophet Marcus Olunde (2 pictures of the speaker to choose from are attached)

6. Contact information: contact@brightmeadowfold.org - Telephone number: 207 583 2914

7. I would also like the following three words on the flyer. These words describe the focus of the event: FIRE, REVIVAL, PROPHETIC

Target Market(s)

Young adults

Font styles to use
Sans Serif

Requirements
Must have
• Logo, speaker's picture
Should not have
• cross image, church image

```html
<!DOCTYPE html>
<html lang="en">
<head>
<meta charset="utf-8">
<title>Kestrel Summit 2020 Flyer</title>
<link href="https://fonts.googleapis.com/css2?family=Anton&family=Bebas+Neue&family=Oswald:wght@400;500;600&family=Dancing+Script:wght@600&display=swap" rel="stylesheet">
<style>
  :root {
    --orange: #f7941d;
    --orange-deep: #e07a10;
    --navy: #2b3566;
    --charcoal: #2a2c36;
    --white: #ffffff;
    --page: #ece7df;
  }
  * { margin: 0; padding: 0; box-sizing: border-box; }
  html, body { width: 1200px; height: 960px; overflow: hidden; background: var(--page); }
  .flyer {
    position: absolute; left: 280px; top: 30px;
    width: 640px; height: 900px; overflow: hidden;
    background: var(--charcoal);
    box-shadow: 0 8px 24px rgba(0,0,0,.18);
  }
  .flyer > * { position: absolute; }
  .glow {
    left: 0; top: 0; width: 640px; height: 420px;
    background:
      radial-gradient(circle at 120px 300px, rgba(247,148,29,.8) 0 22px, transparent 48px),
      radial-gradient(circle at 260px 250px, rgba(247,148,29,.7) 0 18px, transparent 42px),
      radial-gradient(circle at 520px 230px, rgba(255,190,80,.9) 0 26px, transparent 60px),
      radial-gradient(circle at 600px 140px, rgba(247,148,29,.6) 0 18px, transparent 44px),
      radial-gradient(circle at 40px 360px, rgba(247,148,29,.7) 0 20px, transparent 46px),
      radial-gradient(ellipse at 380px 260px, rgba(180,90,20,.55), transparent 65%),
      var(--charcoal);
  }
  .shapes { left: 0; top: 0; }
  .title-block {
    left: 18px; top: 30px; width: 360px; height: 210px;
    background: rgba(43,53,102,.85);
  }
  .title-main {
    left: 30px; top: 30px;
    font-family: "Anton", sans-serif; font-size: 96px; line-height: 1.05;
    color: var(--orange); letter-spacing: 1px;
  }
  .title-sub {
    left: 36px; top: 152px;
    font-family: "Oswald", sans-serif; font-weight: 600; font-size: 44px;
    color: var(--white); letter-spacing: 1px;
  }
  .divider { left: 392px; top: 36px; width: 3px; height: 200px; background: var(--orange); }
  .theme {
    left: 410px; top: 28px; width: 220px;
    font-family: "Anton", sans-serif; font-size: 62px; line-height: 1.15;
    color: var(--orange);
  }
  .theme-and {
    left: 490px; top: 92px;
    font-family: "Dancing Script", cursive; font-size: 40px; color: var(--white);
  }
  .speaker-photo {
    left: 0; top: 330px; width: 330px; height: 460px;
    background: linear-gradient(160deg, #3a2a26 0%, #b8502a 45%, #d8632e 70%, #7a2f1c 100%);
    clip-path: polygon(20% 0, 62% 0, 78% 30%, 100% 45%, 100% 100%, 0 100%, 0 40%);
  }
  .schedule {
    left: 398px; top: 330px; width: 228px;
    font-family: "Bebas Neue", sans-serif; color: var(--navy); line-height: .95;
  }
  .schedule .day { font-size: 46px; }
  .schedule .time { font-size: 20px; margin-bottom: 5px; }
  .schedule .rule { height: 2px; background: var(--orange); margin: 3px 0 7px; }
  .focus {
    left: 150px; top: 490px;
    font-family: "Anton", sans-serif; color: var(--orange); line-height: 1;
    text-shadow: -3px -3px 0 var(--white), 3px -3px 0 var(--white), -3px 3px 0 var(--white), 3px 3px 0 var(--white), 5px 6px 8px rgba(0,0,0,.35);
  }
  .focus .w1 { font-size: 92px; margin-left: 20px; }
  .focus .w2 { font-size: 58px; margin-left: 40px; }
  .focus .w3 { font-size: 60px; }
  .venue {
    left: 430px; top: 632px; width: 200px;
    font-family: "Bebas Neue", sans-serif; color: var(--navy); line-height: 1;
  }
  .venue .name { font-size: 46px; }
  .venue .sub { font-size: 22px; }
  .venue .addr { font-family: "Oswald", sans-serif; font-size: 10px; margin-top: 4px; line-height: 1.3; white-space: nowrap; }
  .brand {
    left: 470px; top: 742px; display: flex; align-items: center; gap: 10px;
  }
  .brand .dot { width: 24px; height: 24px; border-radius: 50%; background: var(--orange); }
  .brand .name { font-family: "Oswald", sans-serif; font-weight: 500; font-size: 34px; line-height: 1.2; color: var(--navy); letter-spacing: 2px; }
  .speaker-band {
    left: 0; top: 790px; width: 440px; height: 62px;
    background: linear-gradient(90deg, var(--navy) 0%, #3c4670 60%, rgba(200,210,220,.9) 100%);
    display: flex; align-items: center; gap: 12px; padding-left: 22px;
  }
  .speaker-band .label { font-family: "Bebas Neue", sans-serif; font-size: 30px; color: var(--orange); }
  .speaker-band .name { font-family: "Oswald", sans-serif; font-weight: 500; font-size: 32px; color: var(--white); }
  .contact-bar {
    left: 0; top: 852px; width: 640px; height: 48px; background: var(--orange);
    display: flex; align-items: center; gap: 12px; padding-left: 22px;
    font-family: "Oswald", sans-serif; font-weight: 600; color: var(--navy); font-size: 20px;
  }
  .contact-bar .label { font-family: "Bebas Neue", sans-serif; font-size: 24px; }
</style>
</head>
<body>
  <div class="flyer">
    <div class="glow"></div>
    <svg class="shapes" width="640" height="900" viewBox="0 0 640 900">
      <path d="M640 300 C420 312 250 400 190 580 L190 900 L640 900 Z" fill="#ffffff"/>
      <path d="M640 268 C420 282 240 372 180 560" fill="none" stroke="#2b3566" stroke-width="34"/>
      <path d="M10 720 C40 520 250 300 640 250" fill="none" stroke="#f7941d" stroke-width="10"/>
    </svg>
    <div class="title-block"></div>
    <div class="title-main">KESTREL</div>
    <div class="title-sub">SUMMIT 2020</div>
    <div class="divider"></div>
    <div class="theme">IN FIRE<br>ON FIRE</div>
    <div class="theme-and">and</div>
    <div class="speaker-photo" role="img" aria-label="Portrait of the speaker in an orange suit and glasses"></div>
    <div class="schedule">
      <div class="day">DECEMBER</div>
      <div class="time">31st @ 6:30 PM</div>
      <div class="rule"></div>
      <div class="day">FRIDAY</div>
      <div class="time">JANUARY 1st | 6:30 PM</div>
      <div class="day">SATURDAY</div>
      <div class="time">2ND @ 6:30 PM</div>
      <div class="day">SUNDAY</div>
      <div class="time">3RD @ 4:30 PM</div>
      <div class="rule"></div>
    </div>
    <div class="focus">
      <div class="w1">FIRE</div>
      <div class="w2">REVIVAL</div>
      <div class="w3">PROPHETIC</div>
    </div>
    <div class="venue">
      <div class="name">HARLOW</div>
      <div class="sub">COMMUNITY CENTER</div>
      <div class="addr">239 Fennimore Street | Portland, ME 04117</div>
    </div>
    <div class="brand">
      <div class="dot"></div>
      <div class="name">VESSARA</div>
    </div>
    <div class="speaker-band">
      <span class="label">SPEAKER:</span>
      <span class="name">Prophet Marcus Olunde</span>
    </div>
    <div class="contact-bar">
      <span class="label">CONTACT INFORMATION:</span>
      <span>207 583 2914</span>
      <span>|</span>
      <span>contact@brightmeadowfold.org</span>
    </div>
  </div>
</body>
</html>
```